Thank you cards for online orders

We have a logo that is attached and I'd for it to be used to make a thank you card that will give our clients some info on product care as well as refund/exchange policy. so maybe a small package that includes a thank you card, and policy details
Updates

Sick

Target Market(s)

Females for 20-70

```html
<!DOCTYPE html>
<html lang="en">
<head>
<meta charset="utf-8">
<title>Kalira – Thank You Cards</title>
<link href="https://fonts.googleapis.com/css2?family=Great+Vibes&family=Alegreya+Sans:wght@400;500&family=Crimson+Text:wght@400;700&family=Cinzel:wght@700&display=swap" rel="stylesheet">
<style>
  :root{
    --backdrop:#e0e0e0;
    --paper:#ffffff;
    --lime:#8dc63f;
    --lime-soft:#c5e08a;
    --sage:#9ea783;
    --sage-dark:#7f8a68;
    --band-dark:#1d1f15;
    --band-olive:#2f3a12;
    --ink:#1a1a1a;
    --grey:#8a8a8a;
  }
  *{margin:0;padding:0;box-sizing:border-box}
  html,body{width:1200px;height:1200px;overflow:hidden;background:var(--backdrop)}
  .card{position:absolute;top:158px;width:498px;height:884px;background:var(--paper);overflow:hidden;box-shadow:0 2px 6px rgba(0,0,0,.25)}
  .card--policy{left:78px}
  .card--brand{left:624px}
  .card__photo{position:absolute;left:0;top:0;width:100%;height:442px}
  .card--policy .card__photo{background:linear-gradient(160deg,#cfe59a 0%,var(--lime-soft) 55%,#b9d97a 100%)}
  .card--brand .card__photo{background:linear-gradient(170deg,#b4bca0 0%,var(--sage) 45%,var(--sage-dark) 100%)}
  .card__band{position:absolute;left:0;top:442px;width:100%;height:152px;background:radial-gradient(ellipse 60% 80% at 50% 20%,var(--band-olive) 0%,var(--band-dark) 75%)}
  .card__rule{position:absolute;left:0;top:606px;width:100%;height:3px;background:var(--lime)}

  .policy{position:absolute;left:28px;top:88px;width:442px;height:290px;transform:rotate(180deg);
    font-family:"Crimson Text",serif;font-size:10.4px;line-height:16px;color:#3a3f2a;text-align:center}
  .policy p{margin-bottom:16px}
  .policy b{font-weight:700;color:var(--ink)}

  .follow{position:absolute;left:0;top:86px;width:100%;height:300px;transform:rotate(180deg);
    display:flex;flex-direction:column;align-items:center;font-family:"Alegreya Sans",sans-serif;color:var(--ink)}
  .follow__title{font-family:"Great Vibes",cursive;font-size:58px;line-height:64px;margin-bottom:22px}
  .follow__dot{width:28px;height:28px;border-radius:50%;background:var(--ink);margin-bottom:10px}
  .follow__handle{font-size:19px;line-height:22px;margin-bottom:22px}

  .thanks{position:absolute;left:0;top:620px;width:100%;text-align:center}
  .thanks__title{font-family:"Great Vibes",cursive;color:var(--lime);font-size:92px;line-height:100px;margin-top:20px}
  .thanks__sub{font-family:"Great Vibes",cursive;color:var(--ink);font-size:28px;line-height:28px;margin:-22px 0 0 -20px}
  .thanks__offer{font-family:"Alegreya Sans",sans-serif;font-size:16.5px;line-height:23px;color:var(--ink);margin-top:34px}
  .thanks__handle{color:var(--lime)}

  .brand{position:absolute;left:0;top:706px;width:100%;text-align:center}
  .brand__name{font-family:"Alegreya Sans",sans-serif;font-weight:400;font-size:50px;letter-spacing:6px;color:var(--lime);line-height:54px}
  .brand__est{font-family:"Cinzel",serif;font-weight:700;font-size:13px;letter-spacing:2px;color:var(--grey);margin-top:8px}
</style>
</head>
<body>

<section class="card card--policy">
  <div class="card__photo" role="img" aria-label="Photo of a woman wearing jewelry, under a light lime tint"></div>
  <div class="policy">
    <p>We value your business, and your complete shopping satisfaction is our priority. If due to some unforeseen situation you are not happy with the product, then the following terms apply for a mutually consented resolution.</p>
    <p>Our policy allows returns from <b>online</b> purchases within 15 days of our ship date for North American customers and 30 days of our ship date for international customers. After those allotted days, the sale is final. To be eligible for a return, your item must be unused, in the original packaging and in the same condition that you received it. To complete your return, we require a receipt or proof of purchase to be emailed to info@kalira.com.</p>
    <p>Please do not send any items back until you receive direct confirmation from our team to go ahead with the return. The customer is responsible for paying for return shipping of items to Kalira.</p>
    <p><b>In-store</b> purchases (including online in-store pickups) are final sale and cannot be returned for a refund. Special circumstances will be reviewed in-store for consideration.</p>
    <p>Please see https://kalira.com/pages/return-policy for more information!</p>
  </div>
  <div class="card__band" role="img" aria-label="Dark band with a lime mandala ornament"></div>
  <div class="card__rule"></div>
  <div class="thanks">
    <div class="thanks__title">Thank you</div>
    <div class="thanks__sub">for your order.</div>
    <p class="thanks__offer">Post it and tag us to receive<br>$25 off your next purchase!<br><span class="thanks__handle">@kalira_jewelry</span></p>
  </div>
</section>

<section class="card card--brand">
  <div class="card__photo" role="img" aria-label="Photo of a woman in a floral top wearing a jeweled necklace, under a sage tint"></div>
  <div class="follow">
    <div class="follow__title">Follow Us</div>
    <div class="follow__dot"></div>
    <div class="follow__handle">kalira_jewelry</div>
    <div class="follow__dot"></div>
    <div class="follow__handle">kalirajewelry</div>
    <div class="follow__dot"></div>
    <div class="follow__handle">kalira</div>
  </div>
  <div class="card__band" role="img" aria-label="Dark band with a lime mandala ornament"></div>
  <div class="card__rule"></div>
  <div class="brand">
    <div class="brand__name">KALIRA</div>
    <div class="brand__est">EST. 2006</div>
  </div>
</section>

</body>
</html>
```